Prospective Client Introduction Brochure/Packet

We need a "Welcome Packet" for a Private Wealth Management Firm to give to prospective clients. It will need to be print ready as it is something we will hand to them or mail to them in a hard copy form. Might even need help designing a few extra pieces. Want a professional piece that share with people, who our firm is, what we do and how we help clients, We will need to provide pics and such but want to narrow down a "look"

Target Market(s)

Business owners and retiree's/ retired individuals

Industry/Entity Type

Financial Services

Font styles to use
Serif
Sans Serif

Colors
0054AA
0677BA
7BADD7
CADEEF
E8F1F8

Requirements
Must have
• Include the KMT logo as best as possible be easy to read
Nice to have
• Flow Chart's of the journey,
Should not have
• Cartoon like images

```html
<!DOCTYPE html>
<html lang="en">
<head>
<meta charset="utf-8">
<title>KMT Wealth Management – Welcome Packet</title>
<link href="https://fonts.googleapis.com/css2?family=Tinos:wght@400;700&display=swap" rel="stylesheet">
<style>
:root{
  --backdrop:#474747;
  --paper:#ffffff;
  --navy:#0f2d6b;
  --navy-deep:#0b2458;
  --ink:#1b1b1b;
  --black-bar:#111111;
  --muted:#3a3a3a;
}
*{box-sizing:border-box;margin:0;padding:0}
html,body{width:900px;height:1200px;overflow:hidden;background:var(--backdrop)}
body{position:relative;font-family:'Tinos',serif;color:var(--ink)}
.page{position:absolute;background:var(--paper);overflow:hidden}
.abs{position:absolute}
.center{text-align:center}

/* footer */
.contact-band{position:absolute;left:0;right:0;height:18px;background:var(--navy);display:flex;align-items:center;justify-content:space-around;padding:0 28px;color:#fff;font-size:5px}
.contact-band.dark{background:var(--black-bar)}
.contact-item{display:flex;align-items:center;gap:3px;white-space:nowrap}
.contact-item svg{width:7px;height:7px}
.web-line{position:absolute;left:0;right:0;text-align:center;font-size:6.5px;letter-spacing:1.6px;color:var(--ink)}

/* page 1 */
.p-welcome{left:73px;top:88px;width:352px;height:497px}
.brand-name{top:20px;left:0;right:0;font-size:27px;color:var(--navy);letter-spacing:1px}
.brand-sub{top:54px;left:0;right:0;font-size:14.5px;color:var(--navy);letter-spacing:1px}
.brand-llc{top:71px;left:0;right:0;font-size:4.5px;color:var(--navy);letter-spacing:1px}
.shore-photo{left:45px;top:93px;width:274px;height:251px;background:linear-gradient(180deg,#e6ebf0 0%,#c4d2dc 30%,#9fb3bf 42%,#cfc6b0 60%,#8f7f66 80%,#6f7a52 100%)}
.photo-frame{left:67px;top:105px;width:270px;height:254px;border:1.5px solid var(--navy)}
.accent-bar{left:57px;top:138px;width:25px;height:144px;background:var(--navy)}
.welcome-title{top:381px;left:0;right:0;font-size:16.5px;font-weight:400;color:var(--navy-deep);letter-spacing:.5px}
.welcome-title b{font-size:18px}
.welcome-copy{top:404px;left:34px;right:34px;font-size:7.2px;line-height:1.3;color:var(--ink)}

/* page 2 */
.p-standard{left:466px;top:88px;width:356px;height:504px}
.office-photo{left:0;top:0;width:356px;height:114px;background:linear-gradient(180deg,#7e8aa3 0%,#a4adc0 35%,#cfd4de 70%,#f4f5f8 100%)}
.top-rule{left:0;right:0;top:114px;height:1.5px;background:var(--navy)}
.kicker{top:122px;left:0;right:0;font-size:10px;color:var(--navy);letter-spacing:.3px}
.headline{top:136px;left:0;right:0;font-size:15.5px;font-weight:400;color:var(--ink)}
.mid-rule{left:0;right:0;top:167px;height:1px;background:var(--navy)}
.intro-copy{top:176px;left:32px;right:32px;font-size:5.5px;line-height:1.3;text-align:justify}
.diff-box{left:21px;top:255px;width:320px;height:189px;border:1.2px solid var(--navy)}
.diff-title{left:52px;top:244px;width:250px;height:23px;background:var(--navy);color:#fff;font-size:10px;display:flex;align-items:center;justify-content:center}
.diff-list{left:18px;top:286px;width:300px;list-style:none}
.diff-list li{position:relative;padding-left:21px;font-size:6.2px;line-height:1.45;min-height:18px;margin-bottom:12px}
.diff-list li::before{content:"";position:absolute;left:0;top:1px;width:10px;height:10px;background:var(--black-bar)}
.diff-list li:nth-child(even)::before{background:var(--navy)}
.diff-list li:nth-child(4),.diff-list li:nth-child(3){margin-bottom:10px}

/* page 3 */
.p-compare{left:73px;top:622px;width:353px;height:493px}
.compare-kicker{top:24px;left:0;right:0;font-size:10px;color:var(--navy)}
.compare-title{top:37px;left:0;right:0;font-size:13px;font-weight:400;color:var(--navy-deep);letter-spacing:.3px}
.compare-rule{left:0;right:0;top:62px;height:1.5px;background:var(--navy)}
.service-bar{position:absolute;left:0;right:0;height:20px;color:#fff;font-size:11px;letter-spacing:.4px;display:flex;align-items:center;justify-content:center;background:var(--navy)}
.service-bar.dark{background:var(--black-bar)}
.service-cols{position:absolute;left:18px;right:14px;display:flex}
.service-cols ul{list-style:none;flex:1}
.service-cols ul+ul{border-left:1px solid #555;padding-left:8px;margin-left:4px}
.service-cols li{position:relative;padding-left:11px;font-size:5px;line-height:1.3;margin-bottom:5px}
.service-cols li::before{content:"";position:absolute;left:0;top:0;width:5px;height:5px;background:var(--black-bar)}
.service-cols li:nth-child(2)::before{background:var(--navy)}

/* page 4 */
.p-commit{left:473px;top:622px;width:345px;height:491px}
.sea-photo{left:0;top:0;width:345px;height:246px;background:linear-gradient(180deg,#3e5466 0%,#8297a8 30%,#b8bcc0 48%,#5f6f74 58%,#3f6f86 75%,#6b97ad 100%)}
.commit-frame{left:72px;top:231px;width:200px;height:34px;border:1px solid var(--navy)}
.commit-title{left:78px;top:237px;width:188px;height:21px;background:var(--navy);color:#fff;font-size:10.5px;letter-spacing:.4px;display:flex;align-items:center;justify-content:center}
.commit-copy{top:272px;left:15px;right:15px;font-size:5.6px;line-height:1.3;color:var(--navy);text-align:justify}
.commit-copy p+p{margin-top:6px}
.checkup-bar{left:38px;top:350px;width:272px;height:22px;background:var(--black-bar);color:#fff;font-size:11.5px;font-weight:700;display:flex;align-items:center;justify-content:center}
.checkup-panel{left:0;right:0;top:378px;height:76px;background:var(--navy);color:#fff}
.checkup-cols{position:absolute;left:15px;right:15px;top:6px;display:flex;gap:12px;font-size:5.3px;line-height:1.3}
.checkup-cols p{flex:1}
.checkup-cols p+p{border-left:1px solid #7d8fb5;padding-left:8px}
.schedule-box{position:absolute;left:78px;top:40px;width:190px;height:26px;border:1px solid #9fb0d0;font-size:5px;text-align:center;padding-top:4px}
.schedule-box strong{display:block;font-size:7.5px;letter-spacing:.4px;margin-top:2px}
</style>
</head>
<body>

<!-- Page 1: welcome cover -->
<section class="page p-welcome">
  <div class="abs brand-name center">KMT</div>
  <div class="abs brand-sub center">WEALTH MANAGEMENT</div>
  <div class="abs brand-llc center">LLC</div>
  <div class="abs shore-photo" role="img" aria-label="Wooden boardwalk stairs leading down to a beach and the sea"></div>
  <div class="abs photo-frame"></div>
  <div class="abs accent-bar"></div>
  <h1 class="abs welcome-title center">WELCOME TO <b>OUR TEAM!</b></h1>
  <p class="abs welcome-copy center">KMT Wealth Management is a comprehensive financial services firm committed to helping our clients improve their long-term financial success. We offer a strong combination of experience and professional client services. We invite you to explore this brochure to compare our services to your current provider.</p>
  <div class="contact-band" style="top:452px">
    <span class="contact-item"><svg viewBox="0 0 10 10"><path d="M5 0a3.5 3.5 0 0 0-3.5 3.5C1.5 6 5 10 5 10s3.5-4 3.5-6.5A3.5 3.5 0 0 0 5 0z" fill="#fff"/><circle cx="5" cy="3.5" r="1.3" fill="#0f2d6b"/></svg>118 Harbor View Lane Suite 210</span>
    <span class="contact-item"><svg viewBox="0 0 10 10"><circle cx="5" cy="5" r="4.3" fill="none" stroke="#fff"/><path d="M3.5 3l1 1-.5 1 1 1 1-.5 1 1-1 1C5 7 3 5 3 4z" fill="#fff"/></svg>(555) 310-6482</span>
    <span class="contact-item"><svg viewBox="0 0 10 10"><circle cx="5" cy="5" r="4.3" fill="none" stroke="#fff"/><path d="M1 5h8M5 .7v8.6M5 .7c-2 2.5-2 6 0 8.6M5 .7c2 2.5 2 6 0 8.6" fill="none" stroke="#fff" stroke-width=".6"/></svg>(555) 310-6495</span>
    <span class="contact-item"><svg viewBox="0 0 10 10"><rect x=".5" y="2" width="9" height="6" fill="none" stroke="#fff"/><path d="M.5 2 5 5.5 9.5 2" fill="none" stroke="#fff"/></svg>info@kmt-wealth.com</span>
  </div>
  <div class="web-line" style="top:478px">www.kmt-wealth.com</div>
</section>

<!-- Page 2: the new standard -->
<section class="page p-standard">
  <div class="abs office-photo" role="img" aria-label="Overhead view of people working at desks in a bright office"></div>
  <div class="abs top-rule"></div>
  <div class="abs kicker center">PERSONALIZED GOLD MEDAL SERVICES</div>
  <h2 class="abs headline center">The New Standard in Wealth Management</h2>
  <div class="abs mid-rule"></div>
  <p class="abs intro-copy">Our approach to delivering holistic financial services always starts and ends with you, our clients. We begin this process by listening to you and discussing your lifestyles, goals, wishes, dreams and family situations. Through a consultative process we then learn the details of your financial picture so we can construct and deliver a customized plan along with properly allocated investment portfolios. Our experienced team of professionals fully evaluates your situation to prepare personal solutions that integrate investment planning, tax reduction planning, retirement income and distribution planning, as well as family wealth planning. We then schedule to meet with you on a regular basis to discuss and update your financial situation and make sure you are on track to reach your goals. We pride ourselves in our superior client services and regular client communications to keep you informed of economic news and appropriate tax law and estate planning rule updates.</p>
  <div class="abs diff-box"></div>
  <div class="abs diff-title">Some of the ways we differ from other firms include:</div>
  <ul class="abs diff-list">
    <li>Our strong menu of Gold Medal Services which include a comprehensive review of your: tax reduction strategies; estate plans; investment plans; retirement plans; and, protection plans.</li>
    <li>Our frequent and regularly scheduled meetings with clients to update your specific plans and discuss your personal situations.</li>
    <li>Our strong and consistent calendar of high quality newsletters, tax reports, and other reports and articles.</li>
    <li>Our frequent schedule of client educational and appreciation events.</li>
    <li>Our personal service that features our best and most current ideas, suggestions and solutions.</li>
  </ul>
  <div class="contact-band" style="top:456px">
    <span class="contact-item"><svg viewBox="0 0 10 10"><path d="M5 0a3.5 3.5 0 0 0-3.5 3.5C1.5 6 5 10 5 10s3.5-4 3.5-6.5A3.5 3.5 0 0 0 5 0z" fill="#fff"/><circle cx="5" cy="3.5" r="1.3" fill="#0f2d6b"/></svg>118 Harbor View Lane Suite 210</span>
    <span class="contact-item"><svg viewBox="0 0 10 10"><circle cx="5" cy="5" r="4.3" fill="none" stroke="#fff"/><path d="M3.5 3l1 1-.5 1 1 1 1-.5 1 1-1 1C5 7 3 5 3 4z" fill="#fff"/></svg>(555) 310-6482</span>
    <span class="contact-item"><svg viewBox="0 0 10 10"><circle cx="5" cy="5" r="4.3" fill="none" stroke="#fff"/><path d="M1 5h8M5 .7v8.6M5 .7c-2 2.5-2 6 0 8.6M5 .7c2 2.5 2 6 0 8.6" fill="none" stroke="#fff" stroke-width=".6"/></svg>(555) 310-6495</span>
    <span class="contact-item"><svg viewBox="0 0 10 10"><rect x=".5" y="2" width="9" height="6" fill="none" stroke="#fff"/><path d="M.5 2 5 5.5 9.5 2" fill="none" stroke="#fff"/></svg>info@kmt-wealth.com</span>
  </div>
  <div class="web-line" style="top:484px">www.kmt-wealth.com</div>
</section>

<!-- Page 3: service comparison -->
<section class="page p-compare">
  <div class="abs compare-kicker center">COMPARE OUR LIST OF GOLD MEDAL SERVICES</div>
  <h2 class="abs compare-title center">TO THE SERVICES YOU RECEIVE TODAY.</h2>
  <div class="abs compare-rule"></div>

  <div class="service-bar" style="top:68px">FINANCIAL PLANNING</div>
  <div class="service-cols" style="top:104px">
    <ul><li>Clients will receive a full comprehensive financial plan</li><li>Discussion and analysis of your financial needs now and in the future</li><li>Analysis of all current and future economic resources</li></ul>
    <ul><li>Continual development and implementation of recommendations to fund your financial needs and help</li><li>maintain a comfortable standard of living.</li></ul>
  </div>

  <div class="service-bar dark" style="top:152px">INVESTMENT OVERSIGHT SERVICE</div>
  <div class="service-cols" style="top:179px">
    <ul><li>Reviewing your investments and designing a personalized portfolio appropriate to your needs</li><li>Year-long, continual monitoring of your investments</li><li>Regular review of your investment accounts to rebalance and manage to your personalized investment strategy</li></ul>
    <ul><li>Reviewing your investments and designing a personalized portfolio appropriate to your needs</li><li>Year-long, continual monitoring of your investments</li><li>Regular review of your investment accounts to rebalance and manage to your personalized investment strategy</li></ul>
  </div>

  <div class="service-bar" style="top:233px">TAX REDUCTION PLANNING</div>
  <div class="service-cols" style="top:264px">
    <ul><li>Complimentary consultation with your tax preparer</li><li>Recommendations of tax solutions including tax advantaged investments</li></ul>
    <ul><li>Special reports on how to help reduce your taxes and other important topics</li><li>Staying up-to-date on new tax laws that can affect your situation</li></ul>
  </div>

  <div class="service-bar dark" style="top:305px">FAMILY WEALTH PLANNING</div>
  <div class="service-cols" style="top:333px">
    <ul><li>Analysis of your current estate plan and concerns</li><li>Complimentary consultation with your attorney</li><li>Assistance in transferring assets to your Living Trust or other trusts</li></ul>
    <ul><li>Analysis of your current estate plan and concerns</li><li>Complimentary consultation with your attorney</li><li>Assistance in transferring assets to your Living Trust or other trusts</li></ul>
  </div>

  <div class="service-bar" style="top:381px">CLIENT SERVICES &amp; COMMUNICATIONS</div>
  <div class="service-cols" style="top:409px">
    <ul><li>Access to our customized online wealth management portal</li><li>Quarterly "market watch" letters detailing our firms research, analysis, and view of the current state of the investment markets</li><li>Economic and educational seminars held throughout the year (guests welcome)</li></ul>
    <ul><li>Access to our customized online wealth management portal</li><li>Quarterly "market watch" letters detailing our firms research, analysis, and view of the current state of the investment markets</li><li>Economic and educational seminars held throughout the year (guests welcome)</li></ul>
  </div>

  <div class="contact-band dark" style="top:469px;height:24px">
    <span class="contact-item"><svg viewBox="0 0 10 10"><path d="M5 0a3.5 3.5 0 0 0-3.5 3.5C1.5 6 5 10 5 10s3.5-4 3.5-6.5A3.5 3.5 0 0 0 5 0z" fill="#fff"/><circle cx="5" cy="3.5" r="1.3" fill="#111"/></svg>118 Harbor View Lane Suite 210</span>
    <span class="contact-item"><svg viewBox="0 0 10 10"><circle cx="5" cy="5" r="4.3" fill="none" stroke="#fff"/><path d="M3.5 3l1 1-.5 1 1 1 1-.5 1 1-1 1C5 7 3 5 3 4z" fill="#fff"/></svg>(555) 310-6482</span>
    <span class="contact-item"><svg viewBox="0 0 10 10"><circle cx="5" cy="5" r="4.3" fill="none" stroke="#fff"/><path d="M1 5h8M5 .7v8.6M5 .7c-2 2.5-2 6 0 8.6M5 .7c2 2.5 2 6 0 8.6" fill="none" stroke="#fff" stroke-width=".6"/></svg>(555) 310-6495</span>
    <span class="contact-item"><svg viewBox="0 0 10 10"><rect x=".5" y="2" width="9" height="6" fill="none" stroke="#fff"/><path d="M.5 2 5 5.5 9.5 2" fill="none" stroke="#fff"/></svg>info@kmt-wealth.com</span>
  </div>
</section>

<!-- Page 4: commitment and check-up offer -->
<section class="page p-commit">
  <div class="abs sea-photo" role="img" aria-label="Rocky coastline at sunset under dramatic cloudy sky"></div>
  <div class="abs commit-frame"></div>
  <div class="abs commit-title">OUR COMMITMENT TO YOU...</div>
  <div class="abs commit-copy">
    <p>KMT Wealth Management was founded with the goal of assisting clients in every aspect of their financial lives. We offer all clients personal, customized service. For each of our clients, we strive to help create financial stability and confidence to provide financial independence.</p>
    <p>Our staff consists of experienced professionals with a "hands on" approach to financial guidance. Our team members are knowledgeable and truly care about helping our clients achieve their goals. We do everything in our power to keep our clients focused on where they want to go, advise them on how to get there, and continually remind them of the importance of maintaining a disciplined approach to realizing their financial goals and dreams.</p>
  </div>
  <div class="abs checkup-bar">COMPLIMENTARY Financial Check-up</div>
  <div class="abs checkup-panel">
    <div class="checkup-cols">
      <p>KMT Wealth Management would like to offer you a complimentary financial check-up. We pride ourselves on providing prompt, personal and highly professional services.</p>
      <p>We want to offer you a <b>complimentary, one-hour, private consultation with one of our professionals at absolutely no cost or obligation to you.</b></p>
    </div>
    <div class="schedule-box">To schedule your complimentary financial check-up, please call<strong>ELEANOR AT (555) 310-6482</strong></div>
  </div>
  <div class="contact-band dark" style="top:468px;height:20px">
    <span class="contact-item"><svg viewBox="0 0 10 10"><path d="M5 0a3.5 3.5 0 0 0-3.5 3.5C1.5 6 5 10 5 10s3.5-4 3.5-6.5A3.5 3.5 0 0 0 5 0z" fill="#fff"/><circle cx="5" cy="3.5" r="1.3" fill="#111"/></svg>118 Harbor View Lane Suite 210</span>
    <span class="contact-item"><svg viewBox="0 0 10 10"><circle cx="5" cy="5" r="4.3" fill="none" stroke="#fff"/><path d="M3.5 3l1 1-.5 1 1 1 1-.5 1 1-1 1C5 7 3 5 3 4z" fill="#fff"/></svg>(555) 310-6482</span>
    <span class="contact-item"><svg viewBox="0 0 10 10"><circle cx="5" cy="5" r="4.3" fill="none" stroke="#fff"/><path d="M1 5h8M5 .7v8.6M5 .7c-2 2.5-2 6 0 8.6M5 .7c2 2.5 2 6 0 8.6" fill="none" stroke="#fff" stroke-width=".6"/></svg>(555) 310-6495</span>
    <span class="contact-item"><svg viewBox="0 0 10 10"><rect x=".5" y="2" width="9" height="6" fill="none" stroke="#fff"/><path d="M.5 2 5 5.5 9.5 2" fill="none" stroke="#fff"/></svg>info@kmt-wealth.com</span>
  </div>
</section>

</body>
</html>
```